Dubai Family protection infographic

We need to produce a way of attracting people to a life insurance and critical illness cover seminar. As this is a pretty dull subject for most people, so we need a cool way of getting people to read the invite/marketing collateral.

We're thinking some kind of colourful and attractive infographic that we can use on flyers and posters as well as online and as an emailer.

Content for the graphic is as bellow:

How much does it cost to replace Mum & Dad?

Mum = Chauffer, Cook, Laundry Service, Household Cleaner, Psychologist, Money Manager

Mums typically work a 94-hour week. At a rather paltry $12 per hour, that’s $4,888 per month – or $58,656 each year. (Source: wagelore.net)

Dad : The average Western Expat’s salary in the Gulf is $12,215 per month. That’s $146,580 each year. (Source: Palmcrest Ledger).

Did you know that the average age of critical illness claimants in the Middle East last year was just 48. Of these, 44% were for cancer while 41% were heart related.

The average age of a death claimant was just 50 years old.
(Source: Verenholt Assurance Group)

1 in 3 people will develop some form of cancer during their lifetime.

That’s 2.36 billion people globally.

And that’s equivalent to the population of China, USA, Brazil, Russia, Philippines, France, UK, South Africa and Italy combined.

Does your family have the resources to hand to cope if a tragedy happens to you?

What can you do to protect them and yourself?

Come to the UAE’s first national protection seminar to find out. Join us at Harbourline Riverside Sports Arena on June 19th at 19:00.

To pre-register, visit www.tovanmere.net/events or alternatively register on the door.

```html
<!DOCTYPE html>
<html lang="en">
<head>
<meta charset="utf-8">
<title>How much does it cost to replace Mum and Dad?</title>
<link rel="stylesheet" href="https://fonts.googleapis.com/css2?family=Roboto+Condensed:wght@400;700;900&family=Open+Sans:wght@400;600;700&display=swap">
<style>
:root{
  --paper:#fdfaf4;
  --maroon:#6e2a1e;
  --orange:#e5622b;
  --teal:#1ba3b6;
  --yellow:#f5b21f;
  --peach:#fbdcb6;
  --rule:#e9b08a;
  --ink-soft:#8a5a48;
}
*{box-sizing:border-box;margin:0;padding:0}
html,body{width:1200px;height:839px;overflow:hidden;background:var(--paper)}
body{font-family:"Open Sans",Arial,sans-serif;color:var(--maroon)}
.canvas{position:relative;width:1200px;height:839px;background:var(--paper)}
.abs{position:absolute}
.headline{left:40px;top:72px;font-family:"Roboto Condensed",Arial,sans-serif;font-weight:700;font-size:37px;line-height:42px;color:var(--maroon);letter-spacing:.3px}
.intro{left:580px;top:62px;width:580px;height:78px;background:var(--peach);padding:14px 22px;font-size:14.5px;line-height:20px;color:var(--orange)}
.section-label{font-size:9px;font-weight:700;color:var(--orange);letter-spacing:.5px;border-top:1px solid var(--rule);padding-top:4px}
.figure{background:var(--orange)}
.display{font-family:"Roboto Condensed",Arial,sans-serif;font-weight:900;line-height:1}
.mums-title{left:120px;top:230px;font-family:"Roboto Condensed",Arial,sans-serif;font-weight:700;font-size:38px;line-height:38px;color:var(--orange)}
.roles{left:120px;top:304px;font-weight:700;font-size:14.5px;line-height:17px;color:var(--orange)}
.small{font-size:11px;line-height:14px;color:var(--orange)}
.tiny{font-size:7px;color:var(--ink-soft)}
.hours{left:90px;top:422px;font-size:112px;color:var(--yellow)}
.hours-label{left:90px;top:535px;font-family:"Roboto Condensed",Arial,sans-serif;font-weight:700;font-size:17px;color:var(--orange);letter-spacing:1px}
.rate{left:40px;top:575px;font-size:84px;color:var(--yellow)}
.rate-label{left:168px;top:588px;font-family:"Roboto Condensed",Arial,sans-serif;font-weight:700;font-size:28px;line-height:28px;color:var(--yellow)}
.dollars{left:40px;top:656px;font-family:"Roboto Condensed",Arial,sans-serif;font-weight:900;font-size:26px;line-height:26px;color:var(--teal);letter-spacing:1px}
.per-month{left:180px;top:660px;font-size:12px;line-height:17px;color:var(--teal)}
.per-month b{color:var(--orange);font-size:16px}
.salary-box{left:420px;top:286px;background:var(--orange);color:#fff;padding:2px 8px;font-size:46px}
.months{left:420px;top:348px;font-family:"Roboto Condensed",Arial,sans-serif;font-weight:700;font-size:20px;letter-spacing:2px;color:var(--orange)}
.dyk-text{left:330px;top:436px;width:170px;font-size:11px;line-height:15px;color:var(--orange)}
.age48{left:500px;top:452px;font-size:42px;color:var(--yellow)}
.pct-label{font-size:11px;line-height:14px;color:var(--orange)}
.pct-label b{font-size:13px}
.big-teal{color:var(--teal)}
.fifty{left:680px;top:168px;font-size:76px}
.years{left:770px;top:180px;font-family:"Roboto Condensed",Arial,sans-serif;font-weight:700;font-size:26px;line-height:28px;color:var(--teal)}
.one-in-three{left:590px;top:282px;background:var(--yellow);color:#fff;padding:2px 8px;font-size:40px}
.billion{left:590px;top:430px;font-size:48px}
.map{left:590px;top:520px;width:250px;height:170px;background:var(--orange);border-radius:6px}
.event{left:850px;top:170px;width:310px;height:620px;background:var(--peach);padding:26px 24px}
.event p{font-family:"Roboto Condensed",Arial,sans-serif;font-weight:700;color:var(--orange);font-size:24px;line-height:28px}
.event .venue{color:var(--maroon);font-size:27px;line-height:30px}
.event .register{margin-top:28px;font-size:21px;line-height:25px}
.event .support{margin-top:26px;font-size:21px;line-height:25px}
.brands{position:absolute;left:24px;bottom:22px;right:24px;display:flex;justify-content:space-between;align-items:center}
.brand{display:flex;align-items:center;gap:6px;font-family:"Roboto Condensed",Arial,sans-serif;font-weight:700;font-size:17px;color:var(--maroon)}
.brand-mark{width:16px;height:16px;background:var(--teal)}
</style>
</head>
<body>
<main class="canvas">
  <h1 class="abs headline">HOW MUCH DOES IT COST<br>TO REPLACE MUM AND DAD?</h1>
  <p class="abs intro">Does your family have the resources to hand to cope if a tragedy happens to you? What can you do to protect them and yourself? Come to the UAE's first national protection seminar to find out.</p>

  <!-- Mums -->
  <div class="abs section-label" style="left:40px;top:198px;width:260px">MUMS</div>
  <div class="abs figure" role="img" aria-label="Icon of a mother figure" style="left:46px;top:228px;width:58px;height:110px;border-radius:29px 29px 6px 6px"></div>
  <div class="abs mums-title">MUM'S<br>ARE:</div>
  <div class="abs roles">Cooks<br>Chauffeurs<br>Psychologists<br>Laundry Services<br>Money Managers<br>Household Cleaners</div>
  <div class="abs small" style="left:40px;top:430px;width:60px">Mum's typically work</div>
  <div class="abs display hours">94</div>
  <svg class="abs" style="left:212px;top:440px" width="72" height="72" viewBox="0 0 72 72" aria-hidden="true">
    <circle cx="36" cy="36" r="31" fill="none" stroke="var(--teal)" stroke-width="6"/>
    <path d="M36 16V36H52" fill="none" stroke="var(--teal)" stroke-width="6" stroke-linecap="round"/>
  </svg>
  <div class="abs hours-label">HOURS PER WEEK</div>
  <div class="abs small" style="left:110px;top:560px">AT</div>
  <div class="abs display rate">$12</div>
  <div class="abs rate-label">PER<br>HOUR</div>
  <div class="abs dollars">$$$$$$<br>$$$$$$</div>
  <div class="abs per-month">that's <b>$4,888</b> per month<br>or <b>$58,656</b><br>each year.</div>
  <div class="abs tiny" style="left:40px;top:716px">Source: wagelore.net</div>

  <!-- Dads -->
  <div class="abs section-label" style="left:310px;top:198px;width:260px">DADS</div>
  <div class="abs figure" role="img" aria-label="Icon of a father figure in a suit" style="left:334px;top:222px;width:66px;height:140px;border-radius:33px 33px 6px 6px"></div>
  <div class="abs small" style="left:420px;top:232px;width:150px;font-size:12px;line-height:15px">The average <b>Western Expat's</b> salary in the Gulf is</div>
  <div class="abs display salary-box">$12,215</div>
  <div class="abs months">PER MONTH</div>
  <div class="abs small" style="left:420px;top:374px">That's <b>$146,580</b> each year.</div>
  <div class="abs tiny" style="left:420px;top:392px">Source: Palmcrest Ledger</div>

  <!-- Did you know -->
  <div class="abs section-label" style="left:310px;top:408px;width:260px">DID YOU KNOW?</div>
  <p class="abs dyk-text">Did you know that the average age of <b>critical illness claimants</b> in the Middle East last year was just <br><br>Of these,</p>
  <div class="abs display age48">48</div>
  <svg class="abs" style="left:330px;top:520px" width="180" height="260" viewBox="0 0 180 260" role="img" aria-label="Chart: 44% of claims for cancer, 41% heart related">
    <polygon points="40,0 140,0 180,60 150,120 30,120 0,60" fill="var(--teal)"/>
    <polygon points="30,126 150,126 128,190 90,260 52,190" fill="var(--yellow)"/>
    <text x="90" y="74" text-anchor="middle" font-family="Roboto Condensed, Arial, sans-serif" font-weight="700" font-size="30" fill="#fff">44%</text>
    <text x="90" y="182" text-anchor="middle" font-family="Roboto Condensed, Arial, sans-serif" font-weight="700" font-size="30" fill="#fff">41%</text>
  </svg>
  <p class="abs pct-label" style="left:520px;top:574px">were for<br><b>cancer</b></p>
  <p class="abs pct-label" style="left:520px;top:676px">were<br><b>heart<br>related.</b></p>

  <!-- Global stats -->
  <p class="abs small" style="left:590px;top:176px;width:88px;color:var(--teal)">The average age of a <b>death claimant</b> was just</p>
  <div class="abs display big-teal fifty">50</div>
  <div class="abs years">YEARS<br>OLD</div>
  <div class="abs tiny" style="left:680px;top:250px">Source: Verenholt Assurance Group</div>
  <div class="abs display one-in-three">1 in 3</div>
  <div class="abs" role="img" aria-label="Icons of three people, one highlighted" style="left:722px;top:282px;width:110px;height:80px;background:linear-gradient(90deg,var(--orange) 0 33%,var(--teal) 33% 66%,var(--orange) 66%);border-radius:8px"></div>
  <p class="abs small" style="left:590px;top:346px;width:120px">people will develop some form of cancer during their lifetime.</p>
  <p class="abs small" style="left:590px;top:408px;font-size:13px">That's</p>
  <div class="abs display big-teal billion">2.36 Billion</div>
  <p class="abs small" style="left:590px;top:486px">people globally.</p>
  <div class="abs map" role="img" aria-label="World map highlighting the countries listed"></div>
  <p class="abs small" style="left:590px;top:724px;width:250px">And that's equivalent to the population of China, USA, Brazil, Russia, Philippines, France, UK, South Africa and Italy combined.</p>

  <!-- Event -->
  <section class="abs event">
    <p>Join us at</p>
    <p class="venue">Harbourline Riverside Sports Arena</p>
    <p>on June 19th at 19:00</p>
    <p class="register">To pre-register, visit www.tovanmere.net/events or alternatively register at the door.</p>
    <p class="support">This event is in support of Marcus Delane's Pedal Onward campaign.</p>
    <div class="brands">
      <span class="brand"><span class="brand-mark"></span>Tovanmere</span>
      <span class="brand">Pedal Onward</span>
    </div>
  </section>
</main>
</body>
</html>
```